Design Health Food E-Book for Small Business Using Provided Content

My business is looking for a designer to design and create an e-book PDF with recipes and images.

The required work will be:

Designing layout of e-book based on provided (below) e-book sample.

Adding supplied recipes and images into a PDF format

Iterating PDF until the work has reached satisfactory requirements

The outcome will be:

1 PDF document (roughly 10-15 pages) created using supplied recipes and images

This recipe e-book by Tessa Morrow should serve as a strong piece of inspiration.

https://brightplatekitchen.example.com/item/7c41d2e9a0f3b615397e8b04

The full content of the e-book, including photos and copy, can be found here:

https://files.example-share.net/sh/kqe915tz47w203x/BBxRnugwXMpoHeTvQjKsZWy4Fb?dl=0

Please arrange for a skype conversation if further clarification of e-book output and/or design are necessary.

Email: rowlet819@mailbrook.net

Industry/Entity Type

Health And Wellness

Font styles to use
Other font styles liked:
• Designer Choice

Requirements
Must have
• Book-like appearance (as in actually looks like a recipe book as opposed to a flyer, photo collection etc.
• Flawless page-linking (from contents page and to external sources) and no errors in text (unless we put a typo in!)
• Cute extra graphics (as per supplied Tessa Morrow book)
Nice to have
• Designer interested in health food
• Experience in e-book design
Should not have
• Typos
• Errors in text linking

```html
<!DOCTYPE html>
<html lang="en">
<head>
<meta charset="utf-8">
<title>The Week Ahead</title>
<link rel="stylesheet" href="https://fonts.googleapis.com/css2?family=Tinos&display=swap">
<style>
  :root {
    --page-bg: #585b6d;
    --page-bg-edge: #545767;
    --ink: #f6f4f3;
    --ornament: #e6c6b4;
  }
  * { margin: 0; padding: 0; box-sizing: border-box; }
  html, body {
    width: 848px;
    height: 1200px;
    overflow: hidden;
    background: var(--page-bg);
  }
  .page {
    position: relative;
    width: 848px;
    height: 1200px;
    background: radial-gradient(ellipse at center, var(--page-bg) 55%, var(--page-bg-edge) 100%);
    font-family: "Tinos", "Times New Roman", serif;
    color: var(--ink);
    overflow: hidden;
  }
  .ornament {
    position: absolute;
    background: radial-gradient(closest-side, rgba(230, 198, 180, 0.28), rgba(230, 198, 180, 0.08) 70%, rgba(230, 198, 180, 0) 100%);
  }
  .ornament--corner { width: 200px; height: 170px; }
  .ornament--top-left { left: -10px; top: -10px; }
  .ornament--top-right { right: -10px; top: -10px; }
  .ornament--bottom-left { left: -10px; bottom: -10px; }
  .ornament--bottom-right { right: -10px; bottom: -10px; }
  .ornament--flower { width: 72px; height: 72px; left: 388px; }
  .ornament--flower-top { top: 24px; }
  .ornament--flower-bottom { bottom: 18px; }
  .ornament--swirl { width: 120px; height: 60px; }
  .ornament--swirl-top-left { left: 250px; top: -10px; }
  .ornament--swirl-top-right { right: 250px; top: -10px; }
  .ornament--swirl-bottom-left { left: 250px; bottom: -8px; }
  .ornament--swirl-bottom-right { right: 250px; bottom: -8px; }

  .week-plan {
    position: absolute;
    left: 0;
    right: 0;
    top: 306px;
    text-align: center;
  }
  .week-plan__title {
    font-weight: 400;
    font-size: 50px;
    line-height: 1;
    letter-spacing: 0.2px;
    margin-left: -4px;
  }
  .week-plan__days {
    margin-top: 78px;
  }
  .week-plan__day {
    font-size: 17.6px;
    line-height: 24px;
    margin-bottom: 24px;
  }
</style>
</head>
<body>
<main class="page">
  <div class="ornament ornament--corner ornament--top-left" role="img" aria-label="Peach swirl flourish ornament, top left corner"></div>
  <div class="ornament ornament--swirl ornament--swirl-top-left" role="img" aria-label="Peach swirl flourish ornament along top edge"></div>
  <div class="ornament ornament--flower ornament--flower-top" role="img" aria-label="Small peach flower ornament, top centre"></div>
  <div class="ornament ornament--swirl ornament--swirl-top-right" role="img" aria-label="Peach swirl flourish ornament along top edge"></div>
  <div class="ornament ornament--corner ornament--top-right" role="img" aria-label="Peach swirl flourish ornament, top right corner"></div>

  <section class="week-plan">
    <h1 class="week-plan__title">The Week Ahead</h1>
    <div class="week-plan__days">
      <p class="week-plan__day">Start your week with a bowl of crunchy, Chocolate Orange Granola and fresh fruits.<br>Preparing your granola on the weekend will let you start your Monday stress-free.</p>
      <p class="week-plan__day">On Tuesday morning, step up your toast game with some (or all) of the nutritious<br>Toast Topper suggestions.</p>
      <p class="week-plan__day">Start your Wednesday with an extra green boost with a Green Galaxy Smoothie Bowl<br>and top with some granola from Monday.</p>
      <p class="week-plan__day">Thursday mornings can be the hardest, so the night before throw together the Carrot<br>Cake Overnight Oats and simply grab from the fridge the next morning.</p>
      <p class="week-plan__day">End your work week with some simple Beetroot Crepes rolled up with<br>your favourite fillings.</p>
      <p class="week-plan__day">Take a little more time to enjoy your weekend recipes with a Warm<br>Buckwheat and Rhubarb Compote Bowl on Saturday.</p>
      <p class="week-plan__day">Sunday wouldn’t be complete without Blueberry Oat Pancakes with a<br>generous glug of maple syrup.</p>
    </div>
  </section>

  <div class="ornament ornament--corner ornament--bottom-left" role="img" aria-label="Peach swirl flourish ornament, bottom left corner"></div>
  <div class="ornament ornament--swirl ornament--swirl-bottom-left" role="img" aria-label="Peach swirl flourish ornament along bottom edge"></div>
  <div class="ornament ornament--flower ornament--flower-bottom" role="img" aria-label="Small peach flower ornament, bottom centre"></div>
  <div class="ornament ornament--swirl ornament--swirl-bottom-right" role="img" aria-label="Peach swirl flourish ornament along bottom edge"></div>
  <div class="ornament ornament--corner ornament--bottom-right" role="img" aria-label="Peach swirl flourish ornament, bottom right corner"></div>
</main>
</body>
</html>
```